Candle company needs a label for candle

Looking for a designer to create my candle label. I am going to attach a few pictures of my vision for the label as well as my Company Logo and jar I have puchased. I'm going for the modern rustic feel but you are the designer and have full trust in your abilities. The label is going to be printed on Kraft paper (2x3) so looking for the font to be black. The candle label MUST include the following information:
Candle Birchway Co.
NO. 01: Eucalyptus + Spearmint
Handmade In NJ
Soy Wax
9oz

Industry/Entity Type

Candle Industry

Colors

Designer to choose colors to be used in the design.

Requirements
Should not have
• Any images

```html
<!DOCTYPE html>
<html lang="en">
<head>
<meta charset="utf-8">
<title>Candle Birchway Co. — No. 01 Eucalyptus + Spearmint Label</title>
<link href="https://fonts.googleapis.com/css2?family=Domine:wght@700&family=Josefin+Sans:wght@400&family=Special+Elite&display=swap" rel="stylesheet">
<style>
  :root {
    --mint: #b4d6cd;
    --mint-deep: #a9c9c2;
    --ink: #000000;
    --paper: #ffffff;
    --accent-red: #e0141e;
  }
  * { margin: 0; padding: 0; box-sizing: border-box; }
  html, body {
    width: 1200px;
    height: 848px;
    overflow: hidden;
    background: var(--paper);
  }
  .board {
    position: relative;
    width: 1200px;
    height: 848px;
  }
  .label-stage {
    position: absolute;
    left: 0; top: 0;
    width: 1200px;
    height: 512px;
    background: linear-gradient(180deg, var(--mint-deep) 0%, var(--mint) 100%);
  }
  .label {
    position: absolute;
    left: 315px;
    top: 66px;
    width: 570px;
    height: 380px;
    background: var(--paper);
    box-shadow: 3px 3px 6px rgba(0, 0, 0, 0.18);
  }
  .label__number {
    position: absolute;
    left: 38px;
    top: 30px;
    font-family: "Josefin Sans", sans-serif;
    font-size: 25px;
    color: var(--ink);
    display: flex;
    align-items: flex-end;
    gap: 6px;
  }
  .label__number-digits {
    font-family: "Special Elite", monospace;
    font-size: 38px;
    line-height: 1;
    color: var(--accent-red);
    border-bottom: 2px solid var(--ink);
    padding: 0 4px 1px 1px;
  }
  .label__scent {
    position: absolute;
    left: 36px;
    top: 96px;
    font-family: "Domine", serif;
    font-weight: 700;
    font-size: 68px;
    line-height: 0.86;
    letter-spacing: -1.5px;
    color: var(--ink);
  }
  .label__rule {
    position: absolute;
    left: 38px;
    top: 289px;
    width: 238px;
    height: 2px;
    background: var(--ink);
  }
  .label__details {
    position: absolute;
    left: 38px;
    top: 299px;
    font-family: "Josefin Sans", sans-serif;
    font-size: 18px;
    line-height: 22px;
    letter-spacing: 1px;
    color: var(--ink);
  }
  .label__brand {
    position: absolute;
    right: 40px;
    bottom: 40px;
    display: flex;
    align-items: center;
    gap: 8px;
    font-family: "Domine", serif;
    font-weight: 700;
    font-size: 16px;
    line-height: 1;
    color: var(--ink);
  }
  .label__brand-square {
    width: 10px;
    height: 10px;
    background: var(--ink);
  }
  .brand-panel {
    position: absolute;
    top: 512px;
    height: 336px;
    display: flex;
    align-items: center;
    justify-content: center;
    gap: 14px;
  }
  .brand-panel--dark { left: 0; width: 600px; background: var(--ink); color: var(--paper); }
  .brand-panel--light { left: 600px; width: 600px; background: var(--paper); color: var(--ink); }
  .brand-panel__square {
    width: 18px;
    height: 18px;
    background: currentColor;
  }
  .brand-panel__name {
    font-family: "Domine", serif;
    font-weight: 700;
    font-size: 30px;
    line-height: 1;
  }
</style>
</head>
<body>
<main class="board">
  <section class="label-stage">
    <article class="label">
      <p class="label__number">No. <span class="label__number-digits">01</span></p>
      <h1 class="label__scent">Eucalyptus +<br>Spearmint</h1>
      <div class="label__rule"></div>
      <p class="label__details">Handmade in New Jersey<br>9 oz. Soy Wax Candle</p>
      <p class="label__brand"><span class="label__brand-square"></span>Candle Birchway Co.</p>
    </article>
  </section>

  <section class="brand-panel brand-panel--dark">
    <span class="brand-panel__square"></span>
    <p class="brand-panel__name">Candle Birchway Co.</p>
  </section>

  <section class="brand-panel brand-panel--light">
    <span class="brand-panel__square"></span>
    <p class="brand-panel__name">Candle Birchway Co.</p>
  </section>
</main>
</body>
</html>
```